All Natural Raw Honey & Goats Milk Body Wash Labels

We have launched a new product line of all natural Raw Honey & Goats Milk body wash with the business name being Vale Orin and the tag line Kindred . Their are currently three line items requiring three labels. Natural (Unscented), Japanese Honeysuckle and Caribbean.
It is a family orientated product that we want to promote as being all natural, healthy and trustworthy. It is an all Australian made product that uses our very own award winning raw honey
I can supply the file for the business name/logo upon request

Families

Bath & body

• a Lux high end feel
• simple easy to read with minimal images
• No cartoons

```html
<!DOCTYPE html>
<html lang="en">
<head>
<meta charset="utf-8">
<title>Vale Orin – Raw Honey &amp; Goats Milk Body Wash Labels</title>
<link rel="stylesheet" href="https://fonts.googleapis.com/css2?family=DM+Serif+Display&family=Montserrat:wght@300;400;500&display=swap">
<style>
  :root {
    --page: #f1e8d6;
    --label-top: #fbfaf6;
    --label-mid: #fbeec4;
    --label-low: #f7e3a4;
    --glow: #f7d97a;
    --ink: #161412;
    --honey: #eab54a;
    --honey-deep: #d98f24;
    --milk: #fdfcf8;
    --pool: #f2d690;
  }
  * { margin: 0; padding: 0; box-sizing: border-box; }
  html, body {
    width: 1200px;
    height: 800px;
    overflow: hidden;
    background: var(--page);
  }
  .canvas {
    width: 1200px;
    height: 800px;
    display: flex;
    align-items: center;
    justify-content: center;
    gap: 36px;
  }
  .label {
    position: relative;
    width: 360px;
    height: 400px;
    background:
      radial-gradient(ellipse 62% 42% at 50% 55%, var(--glow) 0%, rgba(247, 217, 122, 0) 72%),
      linear-gradient(180deg, var(--label-top) 0%, var(--label-mid) 38%, var(--label-low) 100%);
    box-shadow: 0 10px 32px rgba(120, 95, 50, 0.16);
    text-align: center;
    color: var(--ink);
    overflow: hidden;
  }
  .label--honeysuckle { --glow: #f6d58a; --label-low: #f6e0b0; }
  .label--caribbean { --glow: #f5d36e; --label-low: #f3e2a0; }

  .brand {
    position: absolute;
    top: 24px;
    left: 0;
    right: 0;
  }
  .brand-name {
    display: inline-flex;
    align-items: center;
    gap: 7px;
    font-family: "DM Serif Display", serif;
    font-size: 26px;
    line-height: 1;
  }
  .brand-dot {
    width: 8px;
    height: 8px;
    border-radius: 50%;
    background: var(--ink);
  }
  .brand-tagline {
    margin-top: 7px;
    font-family: "Montserrat", sans-serif;
    font-weight: 500;
    font-size: 7px;
    letter-spacing: 0.55em;
    text-transform: uppercase;
  }
  .product-title {
    position: absolute;
    top: 104px;
    left: 0;
    right: 0;
    font-family: "DM Serif Display", serif;
    font-weight: 400;
    font-size: 25px;
    line-height: 1.1;
  }
  .product-type {
    position: absolute;
    top: 164px;
    left: 0;
    right: 0;
    font-family: "Montserrat", sans-serif;
    font-weight: 300;
    font-size: 14px;
    line-height: 1;
  }
  .product-variant {
    position: absolute;
    top: 184px;
    left: 0;
    right: 0;
    font-family: "Montserrat", sans-serif;
    font-weight: 500;
    font-size: 8px;
    letter-spacing: 0.3em;
    text-transform: uppercase;
    line-height: 1;
  }
  .hero-art {
    position: absolute;
    top: 204px;
    left: 40px;
    width: 280px;
    height: 140px;
    background:
      radial-gradient(ellipse 34% 42% at 62% 45%, var(--milk) 0%, rgba(253, 252, 248, 0) 100%),
      radial-gradient(ellipse 30% 32% at 36% 48%, var(--honey-deep) 0%, var(--honey) 45%, rgba(234, 181, 74, 0) 100%),
      radial-gradient(ellipse 60% 22% at 50% 82%, var(--pool) 0%, rgba(242, 214, 144, 0) 100%);
  }
  .volume {
    position: absolute;
    bottom: 14px;
    left: 0;
    right: 0;
    font-family: "DM Serif Display", serif;
    font-size: 13px;
    line-height: 1.25;
  }
</style>
</head>
<body>
  <main class="canvas">
    <section class="label label--natural">
      <header class="brand">
        <div class="brand-name"><span class="brand-dot"></span>Vale Orin</div>
        <div class="brand-tagline">Kindred .</div>
      </header>
      <h1 class="product-title">Raw Honey &amp;<br>Goats Milk</h1>
      <p class="product-type">body wash</p>
      <p class="product-variant">Natural (Unscented)</p>
      <div class="hero-art" role="img" aria-label="Honeycomb pieces and a milk splash above a rippling pool of honey"></div>
      <p class="volume">250ml<br>Net WT. 8.4 FL.OZ</p>
    </section>

    <section class="label label--honeysuckle">
      <header class="brand">
        <div class="brand-name"><span class="brand-dot"></span>Vale Orin</div>
        <div class="brand-tagline">Kindred .</div>
      </header>
      <h1 class="product-title">Raw Honey &amp;<br>Goats Milk</h1>
      <p class="product-type">body wash</p>
      <p class="product-variant">Japanese Honeysuckle</p>
      <div class="hero-art" role="img" aria-label="Honeycomb pieces and a milk splash above a rippling pool of honey"></div>
      <p class="volume">250ml<br>Net WT. 8.4 FL.OZ</p>
    </section>

    <section class="label label--caribbean">
      <header class="brand">
        <div class="brand-name"><span class="brand-dot"></span>Vale Orin</div>
        <div class="brand-tagline">Kindred .</div>
      </header>
      <h1 class="product-title">Raw Honey &amp;<br>Goats Milk</h1>
      <p class="product-type">body wash</p>
      <p class="product-variant">Caribbean</p>
      <div class="hero-art" role="img" aria-label="Honeycomb pieces and a milk splash above a rippling pool of honey"></div>
      <p class="volume">250ml<br>Net WT. 8.4 FL.OZ</p>
    </section>
  </main>
</body>
</html>
```